Marlow Haven

Yoga and Pilates
I teach privates and small groups

Simple clean design 2-4 pages.
(Bookings will be though contacting me, so need for booking capabilities)

```html
<!DOCTYPE html>
<html lang="en">
<head>
<meta charset="utf-8">
<title>Marlow Haven — Yoga and Pilates</title>
<link href="https://fonts.googleapis.com/css2?family=Cinzel:wght@400&family=Montserrat:ital,wght@0,400;0,500;0,600;0,800;1,400&display=swap" rel="stylesheet">
<style>
:root{
  --ink:#1c1c1c;
  --text:#555;
  --accent:#4cc3a6;
  --lilac:#f5f3f9;
  --slate:#7a96a0;
  --dark:#1e1e1e;
  --white:#fff;
}
*{margin:0;padding:0;box-sizing:border-box}
html,body{width:1200px;height:3321px;overflow:hidden;background:var(--white)}
body{font-family:'Montserrat',sans-serif;color:var(--ink);position:relative}
.abs{position:absolute}
.serif{font-family:'Cinzel',serif;font-weight:400}
.btn{position:absolute;border:1.5px solid currentColor;font-family:'Montserrat',sans-serif;font-weight:500;font-size:18px;display:flex;align-items:center;justify-content:center;letter-spacing:.3px;text-decoration:none;color:inherit}

/* header */
.site-header{position:absolute;left:0;top:0;width:1200px;height:108px;background:var(--white)}
.brand{left:113px;top:32px;font-size:36px;letter-spacing:.5px}
.main-nav a{position:absolute;top:45px;font-size:19px;color:var(--ink);text-decoration:none}
.main-nav a.active{color:var(--accent)}
.header-btn{left:945px;top:32px;width:144px;height:51px;font-size:17px;color:var(--ink)}

/* hero */
.hero{position:absolute;left:0;top:108px;width:1200px;height:660px;overflow:hidden}
.hero-photo{position:absolute;inset:0;background:linear-gradient(90deg,#6d8a97 0%,#8fa6b1 30%,#cfd6da 45%,#eef0f1 70%,#f4f4f4 100%)}
.hero-mat{position:absolute;left:170px;top:520px;width:1030px;height:140px;background:linear-gradient(90deg,#6a4fb0,#8b63c9);opacity:.85}
.hero-wave{position:absolute;left:0;top:0}
.hero-title{left:113px;top:210px;font-size:66px;line-height:70px;color:var(--white)}
.hero-sub{left:110px;top:382px;font-size:22px;color:var(--white)}
.hero-btn{left:111px;top:450px;width:182px;height:64px;color:var(--white)}

/* welcome */
.welcome-media{left:111px;top:822px;width:464px;height:305px;background:linear-gradient(120deg,#3b8fd0 0%,#c9a48d 45%,#e7c6b0 60%,#7a8f9a 100%)}
.play{position:absolute;left:199px;top:120px;width:66px;height:66px;border-radius:50%;background:rgba(30,30,30,.8)}
.play svg{position:absolute;left:23px;top:19px}
.ghost{color:rgba(0,0,0,.035);font-family:'Montserrat',sans-serif;font-weight:800;white-space:nowrap}
.ghost-about{left:650px;top:810px;font-size:118px;letter-spacing:8px}
.welcome-title{left:626px;top:814px;font-size:46px;line-height:60px}
.welcome-copy{left:626px;top:950px;width:470px;font-size:15.5px;line-height:28.3px;color:var(--text)}
.read-btn{left:626px;top:1179px;width:151px;height:57px;color:var(--ink)}

/* classes */
.classes{position:absolute;left:0;top:1320px;width:1200px;height:646px;background:var(--lilac);overflow:hidden}
.ghost-classes{left:384px;top:520px;font-size:168px;color:rgba(255,255,255,.95);letter-spacing:6px;font-weight:800}
.section-title{position:absolute;left:0;width:1200px;text-align:center;font-size:44px}
.class-photo{position:absolute;top:178px;width:473px;height:332px}
.class-label{position:absolute;top:536px;width:473px;text-align:center;font-size:27px;font-weight:500}

/* testimonials */
.quote-mark{left:478px;top:2110px;font-family:Georgia,serif;font-size:420px;line-height:420px;color:rgba(0,0,0,.04);font-weight:700}
.quote{left:220px;top:2171px;width:760px;text-align:center;font-style:italic;font-size:24px;line-height:37px;color:#3a3a3a}
.arrow{position:absolute;top:2216px}
.client{left:0;top:2340px;width:1200px;text-align:center;font-size:21px;font-weight:500;letter-spacing:.5px;color:#333}

/* booking */
.book{position:absolute;left:0;top:2444px;width:1200px;height:877px;background:var(--slate);overflow:hidden}
.ghost-book{left:330px;top:20px;font-size:150px;color:rgba(0,0,0,.06);letter-spacing:4px}
.book-title{left:0;top:84px;width:1200px;text-align:center;font-size:46px;color:var(--white)}
.book-copy{left:240px;top:187px;width:720px;text-align:center;font-size:16px;line-height:28px;color:var(--white)}
.book-btn{left:510px;top:277px;width:180px;height:64px;color:var(--white)}
.footer-wave{position:absolute;left:0;top:0}

/* footer */
.social{position:absolute;top:3011px;width:40px;height:40px;border:1.5px solid var(--white);border-radius:50%}
.footer-brand{left:0;top:3072px;width:1200px;text-align:center;font-size:46px;color:var(--white)}
.footer-nav{left:0;top:3151px;width:1200px;display:flex;justify-content:center;gap:31px;font-size:16px;font-weight:500;color:var(--white)}
.footer-contact{left:0;top:3200px;width:1200px;display:flex;justify-content:center;align-items:center;gap:12px;font-size:16.5px;color:var(--white)}
.footer-contact span{display:flex;align-items:center;gap:8px}
.copyright{left:0;top:3247px;width:1200px;text-align:center;font-size:16px;color:#ddd}
</style>
</head>
<body>

<header class="site-header">
  <div class="abs brand serif">MARLOW HAVEN</div>
  <nav class="main-nav">
    <a class="active" style="left:566px">Home</a>
    <a style="left:660px">About</a>
    <a style="left:755px">Classes</a>
    <a style="left:861px">Blog</a>
  </nav>
  <a class="btn header-btn">CONTACT ME</a>
</header>

<section class="hero">
  <div class="hero-photo" role="img" aria-label="Instructor assisting a student in a headstand on a purple mat in a bright studio"></div>
  <div class="hero-mat"></div>
  <svg class="hero-wave" width="1200" height="660" viewBox="0 0 1200 660">
    <path d="M0 660 L0 658 C90 560 220 506 374 513 C520 520 620 640 790 644 C960 648 1110 620 1200 588 L1200 660 Z" fill="#fff"/>
  </svg>
  <h1 class="abs hero-title serif">YOGA AND<br>PILATES</h1>
  <p class="abs hero-sub">For Privates and Small groups</p>
  <a class="btn hero-btn">CONTACT ME</a>
</section>

<section class="welcome">
  <div class="abs welcome-media" role="img" aria-label="Video still of a yoga class stretching together">
    <div class="play"><svg width="24" height="28" viewBox="0 0 24 28"><path d="M0 0 L24 14 L0 28 Z" fill="#fff"/></svg></div>
  </div>
  <div class="abs ghost ghost-about">ABOUT</div>
  <h2 class="abs welcome-title serif">WELCOME TO<br>MARLOW HAVEN</h2>
  <p class="abs welcome-copy">Nemo enim ipsam voluptatem quia voluptas sit aspeatur aut odit aut fugit, sed quia consequuntur magni doloreos qui ratione voluptatem sequi nesciunt. Neque porro quiq uam est, qui dolore m ipsum quia dolor sit amet, consect etur, adipisci velit, sed quia non numquam eius modi tora icidunt ut labore et dolore magnam aliquam quaerat vol uptatluptatem sequi nesciun leque.</p>
  <a class="btn read-btn">READ MORE</a>
</section>

<section class="classes">
  <div class="abs ghost ghost-classes">CLASSES</div>
  <h2 class="section-title serif" style="top:66px">PRIVATE AND SMALL GROUP CLASSES</h2>
  <div class="class-photo" style="left:111px;background:linear-gradient(135deg,#d9d6d2,#8a8683 55%,#3b3a3a)" role="img" aria-label="Group practising downward dog in a yoga studio"></div>
  <div class="class-photo" style="left:616px;background:linear-gradient(135deg,#6b5a4e,#c8a27a 50%,#4a3f3a)" role="img" aria-label="Student seated on a Pilates reformer with an instructor"></div>
  <div class="class-label" style="left:111px">Yoga</div>
  <div class="class-label" style="left:616px">Pilates</div>
</section>

<section class="testimonials">
  <h2 class="section-title serif" style="top:2044px">CLIENT TESTIMONIALS</h2>
  <div class="abs quote-mark">&#8220;</div>
  <svg class="arrow" style="left:148px" width="16" height="28" viewBox="0 0 16 28"><path d="M14 2 L2 14 L14 26" fill="none" stroke="#888" stroke-width="2.5"/></svg>
  <svg class="arrow" style="left:1037px" width="16" height="28" viewBox="0 0 16 28"><path d="M2 2 L14 14 L2 26" fill="none" stroke="#888" stroke-width="2.5"/></svg>
  <p class="abs quote">“ Ut enim ad minima veniam, quis nostrum exercitationem ullam corporis suscipit laboriosam, nisi ut aliquid ex ea comm odi consenima veniaquatur uis au ”</p>
  <div class="abs client">CLARA</div>
</section>

<section class="book">
  <div class="abs ghost ghost-book">BOOK</div>
  <h2 class="abs book-title serif">BOOK YOUR CLASS</h2>
  <p class="abs book-copy">Nemo enim ipsam voluptatem quia voluptas sit aspernatur aut odit aut fugit, sed quia consequuntur magni dolores eos qui ratione voluptatem sequi nesciunt.</p>
  <a class="btn book-btn">CONTACT ME</a>
  <svg class="footer-wave" width="1200" height="877" viewBox="0 0 1200 877">
    <path d="M0 469 C90 512 180 530 300 525 C470 518 620 430 820 395 C960 370 1090 400 1200 534 L1200 877 L0 877 Z" fill="#1e1e1e"/>
  </svg>
</section>

<footer>
  <span class="social" style="left:536px"></span>
  <span class="social" style="left:581px"></span>
  <span class="social" style="left:624px"></span>
  <div class="abs footer-brand serif">MARLOW HAVEN</div>
  <nav class="abs footer-nav"><span>HOME</span><span>ABOUT</span><span>CLASSES</span><span>BLOG</span><span>CONTACT</span></nav>
  <div class="abs footer-contact">
    <span><svg width="12" height="16" viewBox="0 0 12 16"><path d="M6 0C2.7 0 0 2.6 0 5.8 0 10 6 16 6 16s6-6 6-10.2C12 2.6 9.3 0 6 0zm0 8.2A2.4 2.4 0 1 1 6 3.4a2.4 2.4 0 0 1 0 4.8z" fill="#fff"/></svg>No: 123 otam rem aperiam, eaque ipsa</span>
    <span>|</span>
    <span><svg width="14" height="14" viewBox="0 0 14 14"><path d="M3 0 L5 3.5 L3.6 5.2 C4.5 7 6.9 9.4 8.8 10.4 L10.5 9 L14 11 L13 13.6 C6.5 14 0 7.5 0.4 1 Z" fill="#fff"/></svg>1 555 014 2277</span>
    <span>|</span>
    <span><svg width="16" height="12" viewBox="0 0 16 12"><rect width="16" height="12" rx="1.5" fill="#fff"/><path d="M1 1.5 L8 7 L15 1.5" fill="none" stroke="#1e1e1e" stroke-width="1.4"/></svg>info@marlowhaven.com</span>
  </div>
  <p class="abs copyright">© 2020. Marlow Haven. All rights reserved.</p>
</footer>

</body>
</html>
```